Project Sign for Construction Company

Site contractor needs a 4'x8' sign to place on construction sites for advertising. Our company builds the infrastructure for new housing developments. These sign will be posted on the road side to be viewed by passing cars. I want a clean and bold look and feel that resembles my company logo.

Font styles to use
Other font styles liked:
• Hypatia Sans Pro

Colors

Designer to choose colors to be used in the design.

Requirements
Must have
• 555-318-2946 | Info@MarlowTerraworks.example
• CUC 8841907
• www.MarlowTerraworks.example
• Services
• Road Construction
• Site Preparation & Excavation
• Underground Utilities
• Shoreline Restoration
Nice to have
• Now Hiring
• Pipe Layers
• Foremen
• Equipment Operators
Should not have
• Should not have stock picture images used in the design, focus on logo and geometric shapes

```html
<!DOCTYPE html>
<html lang="en">
<head>
<meta charset="utf-8">
<title>Marlow Terraworks – Site Sign</title>
<link rel="stylesheet" href="https://fonts.googleapis.com/css2?family=Bebas+Neue&family=Montserrat:wght@500;600;700&family=Mulish:wght@400;600;700&display=swap">
<style>
  :root {
    --blue-top: #0b539d;
    --blue-bottom: #163f7a;
    --blue-deep: #0f4a92;
    --ink-blue: #25507f;
    --grey-type: #6d6e70;
    --grey-band-a: #5f5f60;
    --grey-band-b: #7a7b7c;
    --red-a: #dc2128;
    --red-b: #9b1a21;
    --white: #ffffff;
    --page: #ebe8e4;
    --heading-grey-a: #d6d6d6;
    --heading-grey-b: #ffffff;
  }
  html, body {
    margin: 0;
    width: 711px;
    height: 1200px;
    overflow: hidden;
    background: var(--page);
  }
  .sign {
    position: absolute;
    left: 57px;
    top: 3px;
    width: 597px;
    height: 1194px;
    background: linear-gradient(180deg, var(--blue-top) 0%, var(--blue-top) 45%, var(--blue-bottom) 100%);
    overflow: hidden;
    font-family: "Mulish", sans-serif;
  }
  .abs { position: absolute; }
  .arch { left: 0; top: 0; }
  .brand-mark {
    left: 213px; top: 40px;
    width: 170px; height: 170px;
    border-radius: 50%;
    background: radial-gradient(circle, #e6eef8 0%, #d3e0f0 100%);
  }
  .brand-name {
    left: 0; width: 597px; top: 228px;
    text-align: center;
    font-family: "Montserrat", sans-serif;
    font-weight: 700;
    font-size: 33px;
    letter-spacing: 1px;
    color: var(--blue-deep);
    margin: 0;
  }
  .brand-tagline {
    left: 0; width: 597px; top: 286px;
    text-align: center;
    font-family: "Montserrat", sans-serif;
    font-weight: 500;
    font-size: 21px;
    letter-spacing: 3.2px;
    color: var(--grey-type);
  }
  .divider {
    left: 0; top: 327px; width: 597px; height: 7px;
    background: var(--grey-type);
  }
  .services-frame { left: 141px; top: 345px; }
  .services-title {
    left: 177px; width: 239px; top: 350px;
    text-align: center;
    font-family: "Bebas Neue", sans-serif;
    font-size: 64px;
    line-height: 64px;
    letter-spacing: 2px;
    margin: 0;
    background: linear-gradient(180deg, var(--heading-grey-b), var(--heading-grey-a));
    -webkit-background-clip: text;
    background-clip: text;
    color: transparent;
  }
  .service-hex { width: 75px; height: 87px; }
  .service-label {
    color: var(--white);
    font-weight: 700;
    font-size: 16px;
    line-height: 22px;
    letter-spacing: 0.6px;
    margin: 0;
  }
  .service-label.light { font-weight: 600; }
  .hiring-frame {
    left: 55px; top: 660px; width: 483px; height: 118px;
    border: 2px solid var(--red-a);
    border-radius: 4px;
  }
  .hiring-banner {
    left: 65px; top: 667px; width: 466px; height: 106px;
    border-radius: 5px;
    background: linear-gradient(90deg, var(--red-a), var(--red-b));
    display: flex; align-items: center; justify-content: center;
  }
  .hiring-title {
    margin: 6px 0 0;
    font-family: "Bebas Neue", sans-serif;
    font-size: 118px;
    line-height: 1;
    letter-spacing: 2px;
    color: var(--white);
    white-space: nowrap;
  }
  .role { width: 146px; height: 165px; }
  .role-label {
    width: 146px;
    text-align: center;
    font-family: "Montserrat", sans-serif;
    font-weight: 600;
    font-size: 16px;
    line-height: 16px;
    letter-spacing: 0.6px;
    color: var(--blue-deep);
    margin: 0;
  }
  .contact-band {
    left: 0; top: 985px; width: 597px; height: 133px;
    background: linear-gradient(180deg, var(--grey-band-a), var(--grey-band-b) 50%, var(--grey-band-a));
  }
  .phone-number {
    left: 166px; top: 1000px;
    font-family: "Bebas Neue", sans-serif;
    font-size: 86px;
    line-height: 1;
    color: var(--white);
    letter-spacing: 1px;
    white-space: nowrap;
  }
  .licence {
    left: 0; width: 597px; top: 1074px;
    text-align: center;
    font-family: "Montserrat", sans-serif;
    font-weight: 700;
    font-size: 31px;
    line-height: 34px;
    letter-spacing: 2px;
    color: var(--white);
  }
  .web-row {
    left: 0; top: 1118px; width: 597px; height: 76px;
    display: flex; align-items: center; justify-content: space-between;
    padding: 0 12px 0 14px; box-sizing: border-box;
    color: var(--white);
    font-size: 15.5px;
    letter-spacing: 0.3px;
  }
  .web-item { display: flex; align-items: center; gap: 6px; white-space: nowrap; }
</style>
</head>
<body>
<main class="sign">

  <svg class="abs arch" width="597" height="334" viewBox="0 0 597 334" aria-hidden="true">
    <path d="M0 334 V285 A298.5 285 0 0 1 597 285 V334 Z" fill="#ffffff"/>
  </svg>

  <div class="abs brand-mark" aria-hidden="true"></div>
  <h1 class="abs brand-name">MARLOW TERRAWORKS</h1>
  <div class="abs brand-tagline">CIVIL CONSTRUCTION</div>
  <div class="abs divider"></div>

  <svg class="abs services-frame" width="310" height="76" viewBox="0 0 310 76" aria-hidden="true">
    <g stroke="#d8e2f0" stroke-width="1" fill="none">
      <line x1="0" y1="8" x2="310" y2="8"/>
      <line x1="0" y1="67" x2="310" y2="67"/>
      <line x1="36" y1="0" x2="36" y2="76"/>
      <line x1="275" y1="0" x2="275" y2="76"/>
    </g>
  </svg>
  <h2 class="abs services-title">SERVICES</h2>

  <!-- Service hexagon shared gradient -->
  <svg width="0" height="0" style="position:absolute" aria-hidden="true">
    <defs>
      <linearGradient id="hexSteel" x1="0" y1="0" x2="0" y2="1">
        <stop offset="0" stop-color="#ffffff"/>
        <stop offset="1" stop-color="#8e9299"/>
      </linearGradient>
    </defs>
  </svg>

  <!-- Road Construction -->
  <svg class="abs service-hex" style="left:14px;top:437px" viewBox="0 0 75 87" aria-hidden="true">
    <path d="M37.5 0 L75 21.75 V65.25 L37.5 87 L0 65.25 V21.75 Z" fill="url(#hexSteel)"/>
    <g fill="none" stroke="#25507f" stroke-width="3">
      <rect x="22" y="25" width="18" height="3" fill="#25507f"/>
      <path d="M25 28 L22 40 H16 V48 M40 28 L44 40 H58 V46"/>
      <circle cx="20" cy="52" r="5.5"/>
      <circle cx="50" cy="50" r="9"/>
      <circle cx="50" cy="50" r="3" fill="#25507f"/>
    </g>
  </svg>
  <p class="abs service-label" style="left:96px;top:469px">Road Construction</p>

  <!-- Underground Utilities -->
  <svg class="abs service-hex" style="left:298px;top:437px" viewBox="0 0 75 87" aria-hidden="true">
    <path d="M37.5 0 L75 21.75 V65.25 L37.5 87 L0 65.25 V21.75 Z" fill="url(#hexSteel)"/>
    <g fill="none" stroke="#25507f" stroke-width="2.4" stroke-linecap="round">
      <path d="M20 22 a6 6 0 0 0 6 10 L52 62"/>
      <path d="M55 26 L24 60"/>
      <rect x="47" y="19" width="14" height="7" transform="rotate(42 54 22)"/>
    </g>
  </svg>
  <p class="abs service-label" style="left:381px;top:469px">Underground Utilities</p>

  <!-- Site Preparation & Excavation -->
  <svg class="abs service-hex" style="left:14px;top:535px" viewBox="0 0 75 87" aria-hidden="true">
    <path d="M37.5 0 L75 21.75 V65.25 L37.5 87 L0 65.25 V21.75 Z" fill="url(#hexSteel)"/>
    <g fill="none" stroke="#25507f" stroke-width="2.4" stroke-linecap="round">
      <path d="M24 26 L56 60"/>
      <rect x="16" y="20" width="11" height="8" transform="rotate(45 21 24)"/>
      <path d="M54 24 L20 62"/>
      <path d="M44 20 Q56 18 60 32"/>
    </g>
  </svg>
  <p class="abs service-label" style="left:96px;top:558px">Site Preparation &amp;<br>Excavation</p>

  <!-- Shoreline Restoration -->
  <svg class="abs service-hex" style="left:298px;top:535px" viewBox="0 0 75 87" aria-hidden="true">
    <path d="M37.5 0 L75 21.75 V65.25 L37.5 87 L0 65.25 V21.75 Z" fill="url(#hexSteel)"/>
    <g fill="none" stroke="#25507f" stroke-width="4">
      <path d="M22 44 A19 19 0 1 1 30 58"/>
    </g>
    <path d="M13 42 H31 L22 52 Z" fill="#25507f"/>
    <circle cx="40" cy="42" r="4" fill="#25507f"/>
  </svg>
  <p class="abs service-label light" style="left:381px;top:570px">Shoreline Restoration</p>

  <div class="abs hiring-frame"></div>
  <div class="abs hiring-banner"><h2 class="hiring-title">NOW HIRING</h2></div>

  <!-- Pipe Layers -->
  <svg class="abs role" style="left:69px;top:789px" viewBox="0 0 146 165" aria-hidden="true">
    <path d="M73 12 L140 50 V124 L73 163 L6 124 V50 Z" fill="#1a4480" stroke="#9aa0a8" stroke-width="2"/>
    <path d="M66 0 L133 38 V114 L66 153 L0 114 V38 Z" fill="#ffffff"/>
    <path d="M66 34 L108 52 L66 70 L24 52 Z" fill="none" stroke="#0f4a92" stroke-width="9" stroke-linejoin="round"/>
    <path d="M24 66 L66 84 L108 66" fill="none" stroke="#0f4a92" stroke-width="9" stroke-linejoin="round" stroke-linecap="round"/>
  </svg>
  <p class="abs role-label" style="left:62px;top:887px">Pipe Layers</p>

  <!-- Foremen -->
  <svg class="abs role" style="left:228px;top:789px" viewBox="0 0 146 165" aria-hidden="true">
    <path d="M73 12 L140 50 V124 L73 163 L6 124 V50 Z" fill="#1a4480" stroke="#9aa0a8" stroke-width="2"/>
    <path d="M66 0 L133 38 V114 L66 153 L0 114 V38 Z" fill="#ffffff"/>
    <g fill="none" stroke="#25507f" stroke-width="3" stroke-linejoin="round">
      <path d="M49 30 A17 17 0 0 1 83 30 H87 V35 H45 V30 Z"/>
      <rect x="60" y="11" width="12" height="7" rx="2"/>
      <path d="M42 68 Q44 56 66 54 Q88 56 90 68"/>
      <rect x="32" y="66" width="68" height="27" rx="3"/>
    </g>
  </svg>
  <p class="abs role-label" style="left:222px;top:887px">Foremen</p>

  <!-- Equipment Operators -->
  <svg class="abs role" style="left:388px;top:789px" viewBox="0 0 146 165" aria-hidden="true">
    <path d="M73 12 L140 50 V124 L73 163 L6 124 V50 Z" fill="#1a4480" stroke="#9aa0a8" stroke-width="2"/>
    <path d="M66 0 L133 38 V114 L66 153 L0 114 V38 Z" fill="#ffffff"/>
    <g fill="none" stroke="#25507f" stroke-width="4" stroke-linejoin="round">
      <path d="M44 58 V24 H82 M52 52 V32 H76"/>
      <path d="M36 60 H78 V66 H36 Z" fill="#25507f"/>
      <path d="M44 66 V88 M74 66 V88"/>
      <circle cx="90" cy="31" r="6"/>
      <path d="M80 44 H98 V66 H92 L90 86 H82 L80 66 Z"/>
    </g>
  </svg>
  <p class="abs role-label" style="left:381px;top:880px;line-height:15px">Equipment<br>Operators</p>

  <div class="abs contact-band"></div>
  <svg class="abs" style="left:92px;top:1003px" width="61" height="62" viewBox="0 0 24 24" aria-hidden="true">
    <path fill="#ffffff" d="M6.6 2.2 9.3 6.5c.4.7.3 1.5-.3 2L7.6 9.8c1.3 2.8 3.8 5.3 6.6 6.6l1.3-1.4c.5-.6 1.3-.7 2-.3l4.3 2.7c.7.4 1 1.3.6 2l-1 2c-.6 1.1-1.9 1.7-3.1 1.4C10 21.4 2.6 14 1.2 6.7.9 5.5 1.5 4.2 2.6 3.6l2-1c.7-.4 1.6-.1 2 .6Z"/>
  </svg>
  <div class="abs phone-number">555 318 2946</div>
  <div class="abs licence">CUC 8841907</div>

  <footer class="abs web-row">
    <span class="web-item">
      <svg width="24" height="17" viewBox="0 0 24 17" aria-hidden="true">
        <rect width="24" height="17" rx="2" fill="#ffffff"/>
        <path d="M1 2 L12 10 L23 2" fill="none" stroke="#163f7a" stroke-width="2"/>
      </svg>
      Info@MarlowTerraworks.example
    </span>
    <span class="web-item">
      <svg width="16" height="16" viewBox="0 0 16 16" aria-hidden="true">
        <g fill="none" stroke="#ffffff" stroke-width="1.2">
          <circle cx="8" cy="8" r="7"/>
          <ellipse cx="8" cy="8" rx="3" ry="7"/>
          <path d="M1 8 H15 M2.5 4.5 H13.5 M2.5 11.5 H13.5"/>
        </g>
      </svg>
      www.MarlowTerraworks.example
    </span>
  </footer>

</main>
</body>
</html>
```